1 page A4 double sided Brochure Design Folded to envelope size. Interesting fold design would be co

Small family run guesthouse BnB in Blue Mountains Australia needs a new brochure showing different aspects of business

We need a new brochure to go with our new website. Basically the design would be good as a double sided brochure that can be folded down to standard envelope size.

We have seen a few interesting brochure designs before that fold in different ways (and therefore have the design to match) but still fold down to this size to help with postage.

The design would have to showcase the different aspects of our business including individual accommodation for couples and families, conference market, wedding market, retreat market and events market (parties, re-unions etc). The Business must be Showcased as The Fernhollow Lodge, Blue Mountains

It is possible to arrange design so folds separate different sections of info/pictures.

It is also optional that we possibly have 2 brochures instead, one that is a basic all inclusive once described and one that only deals with group bookings (wedding conference retreats etc etc)

Must match design elements from our web page. Feel free to take informations, elements and images from there for design www.fernhollowlodge.com.au

Here is a link to our view we wake up to every morning to inspire all those working on a design!
http://www.fernhollowlodge.com.au/images/view.jpg

Target Market(s)

Group bookings, weddings, conferences, retreats, events and Blue Mountains Travellers

Industry/Entity Type

Accommodation

Requirements
Must have
• Must be based on our current websites design feel, colours, etc
Must be showcased as The Fernhollow Lodge Blue Mountains.
Must mention The Blue Mountains as a world heritage destination
Must be A4 double sided that can fold down to 1/3 the size to fit into a standard envelope. Any designs that will not fit in a standard envelope once folded can not be accepted as they are outside the brief
Nice to have
• Interesting folding design to get people interested to read it.

```html
<!DOCTYPE html>
<html lang="en">
<head>
<meta charset="utf-8">
<title>The Fernhollow Lodge – Brochure Cover</title>
<link rel="stylesheet" href="https://fonts.googleapis.com/css2?family=Tinos:wght@700&family=Arimo:wght@400;700&family=Carlito&display=swap">
<style>
  :root {
    --sky-deep: #3f6fd8;
    --sky-mid: #5b8ef0;
    --sky-light: #a9c8f6;
    --mist: #e9f1fc;
    --navy: #0f1e48;
    --ink: #0c1428;
    --title-yellow: #fff200;
    --url-lime: #d6f23c;
    --white: #ffffff;
    --trim-red: #d8262c;
    --photo-green: #3f5a2a;
    --photo-sky: #dfe9ef;
    --ornament-band: #9cbdf0;
  }
  * { margin: 0; padding: 0; box-sizing: border-box; }
  html, body {
    width: 1200px; height: 2535px; overflow: hidden;
    background: var(--white);
  }
  .cover {
    position: relative; width: 1200px; height: 2535px; overflow: hidden;
    background: linear-gradient(180deg, var(--sky-deep) 0%, var(--sky-mid) 20%, var(--sky-light) 60%, var(--mist) 100%);
  }
  .swooshes { position: absolute; inset: 0; width: 1200px; height: 2535px; }

  .brand-mark {
    position: absolute; left: 872px; top: 131px; width: 200px; height: 240px;
    display: flex; flex-direction: column; align-items: center; justify-content: center; gap: 16px;
    text-align: center;
  }
  .brand-mark .square { width: 44px; height: 44px; background: var(--white); }
  .brand-mark .name {
    font-family: "Tinos", serif; font-weight: 700; font-size: 30px; line-height: 1.15;
    color: var(--white);
  }

  .title-band {
    position: absolute; left: 0; top: 554px; width: 1200px; height: 350px;
    background: var(--navy); text-align: center; padding-top: 36px;
  }
  .title-band h1 {
    font-family: "Tinos", serif; font-weight: 700; font-size: 108px; line-height: 1.0;
    color: var(--title-yellow);
  }
  .title-band .tagline {
    font-family: "Arimo", sans-serif; font-weight: 400; font-size: 46px;
    color: var(--white); margin-top: 6px;
  }

  .ornament {
    position: absolute; left: 0; width: 1200px; height: 150px;
    background: linear-gradient(90deg, rgba(156,189,240,0.55), rgba(200,215,240,0.75) 50%, rgba(156,189,240,0.55));
  }
  .ornament.upper { top: 904px; }
  .ornament.lower { top: 1855px; }

  .view-photo {
    position: absolute; left: 0; top: 1057px; width: 1200px; height: 798px;
    background: linear-gradient(180deg, var(--photo-sky) 0%, #b9c9b4 22%, #5f7a45 40%, var(--photo-green) 70%, #4f7b2e 100%);
  }

  .services {
    position: absolute; left: 0; top: 2060px; width: 1200px;
    display: grid; grid-template-columns: 520px 420px; column-gap: 60px;
    padding-left: 180px;
    font-family: "Carlito", sans-serif; font-size: 52px; line-height: 62px; color: var(--ink);
  }
  .services ul { list-style: none; }
  .services .col-left li:nth-child(2) { padding-left: 88px; }
  .services .col-left li:nth-child(3) { padding-left: 122px; }
  .services .col-right li:nth-child(1) { padding-left: 16px; }
  .services .col-right li:nth-child(2), .services .col-right li:nth-child(3) { padding-left: 0; }

  .web-band {
    position: absolute; left: 0; top: 2350px; width: 1200px; height: 185px;
    background: var(--ink); display: flex; align-items: center; justify-content: center;
  }
  .web-band .url {
    font-family: "Arimo", sans-serif; font-weight: 700; font-size: 52px; color: var(--url-lime);
    margin-top: -18px;
  }

  .trim-line {
    position: absolute; left: 4px; top: 59px; width: 1138px; height: 2473px;
    border: 2px solid var(--trim-red); pointer-events: none;
  }
</style>
</head>
<body>
<main class="cover">
  <svg class="swooshes" viewBox="0 0 1200 2535" aria-hidden="true">
    <path d="M0 0 H520 C640 180 700 380 760 554 H0 Z" fill="#4a7fe6" opacity="0.5"/>
    <path d="M640 0 C760 160 840 360 900 554 H960 C880 340 800 150 700 0 Z" fill="#c6dcfb" opacity="0.55"/>
    <path d="M760 0 C880 170 960 360 1010 554 H1040 C990 340 900 150 800 0 Z" fill="#ffffff" opacity="0.35"/>
    <path d="M0 0 C200 120 420 300 520 554 H440 C360 330 180 150 0 60 Z" fill="#7aa6f2" opacity="0.35"/>
    <path d="M920 904 C1000 960 1080 1000 1200 1010 V904 Z" fill="#3d6fd6" opacity="0.6"/>
    <path d="M1060 1855 C1110 2050 1130 2200 1140 2350 H1200 V1855 Z" fill="#2f6ee0"/>
    <path d="M1100 1855 C1150 2050 1170 2200 1180 2350 H1200 V1855 Z" fill="#6fc8ef"/>
    <path d="M1080 1900 C1120 2080 1140 2220 1150 2350 H1160 C1150 2200 1130 2060 1090 1900 Z" fill="#ffffff" opacity="0.7"/>
  </svg>

  <div class="brand-mark">
    <span class="square"></span>
    <span class="name">The Fernhollow Lodge Blue Mountains</span>
  </div>

  <header class="title-band">
    <h1>The Fernhollow<br>Lodge</h1>
    <p class="tagline">a world heritage destination</p>
  </header>

  <div class="ornament upper" role="img" aria-label="Decorative silver scrollwork border"></div>

  <div class="view-photo" role="img" aria-label="Photograph of the bushland lookout over the Blue Mountains valley from the lodge"></div>

  <div class="ornament lower" role="img" aria-label="Decorative silver scrollwork border"></div>

  <section class="services" aria-label="Services">
    <ul class="col-left">
      <li>Accommodation</li>
      <li>Conference</li>
      <li>Functions</li>
    </ul>
    <ul class="col-right">
      <li>Group Stays</li>
      <li>Weddings</li>
      <li>Retreats</li>
    </ul>
  </section>

  <footer class="web-band">
    <span class="url">www.fernhollowlodge.com.au</span>
  </footer>

  <div class="trim-line" aria-hidden="true"></div>
</main>
</body>
</html>
```